Launching new podcast and need artwork

we are two guys in our early 40's from east Texas who are starting a podcast around personal finance.

The title of the podcast will be "Coin Porchlight" and the subtitle will be "Money tricks with a little front-porch drawl"

We own the company brightharborplans.com and will be using the podcast as a lead generation for our primary business of financial coaching.

Target Market(s)

Male 35-45 years old

Industry/Entity Type

Personal finance

Requirements
Nice to have
• Rugged or rustic feel would fit our personas

```html
<!DOCTYPE html>
<html lang="en">
<head>
<meta charset="utf-8">
<title>Coin Porchlight — Podcast Cover</title>
<link rel="stylesheet" href="https://fonts.googleapis.com/css2?family=Bebas+Neue&display=swap">
<style>
  :root {
    --bg: #1f1f1f;
    --green: #8cc63f;
    --blue: #3f6b9f;
  }
  html, body {
    margin: 0;
    padding: 0;
    width: 1200px;
    height: 1200px;
    overflow: hidden;
    background: var(--bg);
  }
  .cover {
    display: block;
    width: 1200px;
    height: 1200px;
  }
  .cover-text {
    font-family: "Bebas Neue", "Oswald", sans-serif;
    text-anchor: middle;
  }
  .title-top { fill: var(--green); font-size: 377px; }
  .title-bottom { fill: var(--blue); font-size: 260px; }
  .tagline-top { fill: var(--green); font-size: 67px; }
  .tagline-bottom { fill: var(--blue); font-size: 67px; }
</style>
</head>
<body>
  <svg class="cover" viewBox="0 0 1200 1200" xmlns="http://www.w3.org/2000/svg" role="img" aria-label="Coin Porchlight — Money tricks with a little front-porch drawl">
    <rect width="1200" height="1200" fill="var(--bg)"/>
    <text class="cover-text title-top" x="578" y="544">COIN</text>
    <text class="cover-text title-bottom" x="578" y="772">PORCHLIGHT</text>
    <text class="cover-text tagline-top" x="580" y="910">MONEY TRICKS</text>
    <text class="cover-text tagline-bottom" x="578" y="969">WITH A LITTLE FRONT-PORCH DRAWL</text>
  </svg>
</body>
</html>
```